Zielgruppe
Die Kessler-Volkshochschule Kreis Aurental ist eine gemeinnützige Einrichtung zur Erwachsenen- und Weiterbildung mit ca. 5.000 Veranstaltungen pro Jahr.
Volkshochschulen sind entgegen ihrer Bezeichnung keine Hochschulen oder Schulen, sondern in Deutschland dem Bildungsbereich der Weiterbildung zugeordnet.
Aufgabenstellung
Die Kessler-Volkshochschule Kreis Aurental möchte mit einer neuen Webseite, welche auch für mobile Geräte geeignet sein muss, Ihren neuen Internetauftritt umsetzen.
Vorgaben:
- der Internetauftritt soll modern gestaltet sein.
- die unter Dateien befindlichen Guidelines müssen eingehalten werden. Wichtig hierbei ist, dass die 6 Symbole auf die Startseite für die Auswahl der jeweiligen Kursbereiche integriert werden. Hierbei ist zu beachten, dass die Anzahl der Symbole erweiterbar ist.
Als CMS wird Typo3 genutzt.
Es geht um die Erstellung der Startseite auf welcher auch News untergebracht werden sollen - ggf. in Kachelform. Und die Erstellung einer Unterseite.

```html
<!DOCTYPE html>
<html lang="de">
<head>
<meta charset="utf-8">
<title>Kessler-Volkshochschule Kreis Aurental</title>
<link href="https://fonts.googleapis.com/css2?family=Arimo:wght@400;700&display=swap" rel="stylesheet">
<style>
:root{
  --navy:#0b3272;
  --navy-deep:#062a5e;
  --steel:#2c5387;
  --slate:#4a5b76;
  --light:#ebebec;
  --ink:#1d2a44;
  --text-grey:#6c7385;
  --white:#fff;
  --beruf:#5bb7e6;--sprachen:#8a5ba8;--gesundheit:#a8c70e;--kultur:#e3001b;--gesellschaft:#ee6a0c;--grundbildung:#f6b800;
}
*{box-sizing:border-box;margin:0;padding:0}
html,body{width:873px;height:1200px;overflow:hidden;background:var(--white)}
body{font-family:"Arimo",Arial,sans-serif;color:var(--ink)}
.page{position:absolute;left:0;top:0;width:1480px;height:2034px;transform:scale(.5899);transform-origin:0 0}
.abs{position:absolute}
a{color:inherit}

.brand{left:140px;top:50px;display:flex;align-items:center;gap:14px}
.brand-dot{width:22px;height:22px;border-radius:50%;background:var(--navy)}
.brand-name{font-size:20px;line-height:24px;color:var(--navy);border-left:1px solid #ccd;padding-left:14px}
.brand-name span{display:block;color:var(--text-grey);letter-spacing:.5px}
.search{left:992px;top:40px;width:348px;height:33px;border-bottom:1.5px solid var(--navy);color:#9aa3b5;font-size:17px;padding-top:6px}
.search svg{position:absolute;right:0;top:0}
.meta-nav{left:993px;top:80px;width:348px;display:flex;justify-content:space-between;font-size:18px;color:var(--navy)}
.main-nav{left:140px;top:140px;display:flex;gap:38px;font-size:18px;color:var(--navy)}
.main-nav span::after{content:"";display:inline-block;width:6px;height:6px;border-right:2px solid var(--navy);border-bottom:2px solid var(--navy);transform:rotate(45deg);margin-left:8px;position:relative;top:-4px}

.photo-left{left:140px;top:177px;width:300px;height:740px;background:linear-gradient(160deg,#e9e7e4 0%,#c9b9a9 40%,#8f8f93 100%)}
.photo-center{left:440px;top:177px;width:600px;height:440px;background:linear-gradient(110deg,#ccb9a6 0%,#e7c8b1 35%,#6f5f55 75%,#3d3732 100%)}
.tile{color:var(--white)}
.tile h2{font-size:31px;line-height:32px;font-weight:700}
.tile p{font-size:17px;line-height:24px;margin-top:12px;letter-spacing:.3px}
.portal{left:1040px;top:177px;width:300px;height:440px;background:linear-gradient(180deg,#0b3a7d,#062a5e);padding:46px 30px}
.field{width:240px;height:50px;background:var(--white);color:#a8aebb;font-size:17px;padding:16px 19px;margin-top:22px}
.field+.field{margin-top:12px}
.portal-links{margin-top:28px;font-size:12px;line-height:20px}
.portal-links a{display:block;text-decoration:underline}
.btn{position:absolute;right:0;bottom:0;background:var(--white);color:var(--ink);font-weight:700;font-size:16px;padding:10px 19px 9px}
.notch::before{content:"";position:absolute;left:-20px;top:50%;margin-top:-25px;border:25px solid transparent;border-left:0;border-right-width:20px;border-right-color:inherit}
.akademie{left:440px;top:617px;width:300px;height:300px;background:var(--steel);border-color:var(--steel);padding:44px 29px}
.brochure{left:740px;top:617px;width:300px;height:300px;background:linear-gradient(160deg,#fff 0%,#fff 36%,#dfe9f4 50%,#8ab8e0 100%)}
.program{left:1040px;top:617px;width:300px;height:300px;background:var(--steel);border-color:var(--steel);padding:44px 29px}

.courses-head{left:140px;top:967px;width:1200px;height:83px;background:linear-gradient(90deg,#0b3a7d,#062a5e);color:var(--white);font-size:31px;font-weight:700;padding:24px 30px}
.courses-head::after{content:"";position:absolute;left:50px;bottom:-19px;border:27px solid transparent;border-top:19px solid #0a377a;border-bottom:0}
.courses{left:140px;top:1050px;width:1200px;height:230px;background:var(--light)}
.arrow-btn{position:absolute;top:42px;width:30px;height:98px;background:#e3e3e5;color:var(--navy);font-size:38px;font-weight:700;text-align:center;line-height:96px}
.course{position:absolute;top:32px;width:170px;text-align:center;font-size:20px;font-weight:700}
.circle{width:128px;height:128px;border-radius:50%;border:4px solid var(--white);margin:0 auto 30px}

.news-head{left:140px;top:1330px;width:300px;height:300px;background:linear-gradient(180deg,#0b3a7d,#062a5e);padding:46px 30px}
.news-list{left:440px;top:1330px;width:300px;height:600px;background:var(--light);padding:46px 29px}
.news-item{margin-bottom:44px}
.news-item h3{font-size:24px;font-weight:700;color:var(--ink)}
.news-item p{font-size:17px;line-height:24px;color:#4a4f5c;margin-top:12px;letter-spacing:.3px}
.news-item a{display:inline-block;margin-top:10px;font-size:18px;color:#4a4f5c;border-bottom:1px solid #4a4f5c;text-decoration:none;line-height:22px}
.news-list::before{content:"";position:absolute;left:0;top:125px;border:25px solid transparent;border-right:0;border-left:20px solid #07306a}
.jobs{left:140px;top:1630px;width:300px;height:300px;background:var(--slate);padding:44px 30px}
.date{left:740px;top:1330px;width:300px;height:300px;background:var(--slate);color:#e4e4e8}
.date::after{content:"";position:absolute;right:-20px;top:125px;border:25px solid transparent;border-right:0;border-left:20px solid var(--slate);z-index:2}
.date .day{position:absolute;left:24px;top:20px;font-size:210px;font-weight:700;letter-spacing:-8px;line-height:210px}
.date .month{position:absolute;left:29px;top:222px;font-size:31px;font-weight:700}
.calendar{left:1040px;top:1330px;width:300px;height:300px;background:var(--light);padding:46px 29px;color:var(--text-grey)}
.calendar h4{font-size:25px;font-weight:700;color:var(--ink)}
.cal-nav{position:absolute;right:27px;top:52px;display:flex;gap:6px}
.cal-nav span{width:22px;height:16px;background:var(--slate)}
.days{display:grid;grid-template-columns:repeat(7,36.7px);font-size:22px;row-gap:10px;margin-top:12px}
.days span{text-align:center;line-height:28px}
.days .today{background:var(--slate);color:var(--white)}
.top{left:740px;top:1630px;width:300px;height:300px;background:linear-gradient(180deg,#0b3a7d,#062a5e);padding:44px 29px}
.top::after{content:"";position:absolute;right:-20px;top:125px;border:25px solid transparent;border-right:0;border-left:20px solid #072c63;z-index:2}
.photo-dance{left:1040px;top:1630px;width:300px;height:300px;background:linear-gradient(150deg,#3d2b1c 0%,#6b4e34 40%,#d9c3a0 65%,#2a2019 100%)}

.footer{left:140px;top:1980px;width:1200px;height:54px;background:var(--navy);color:var(--white);font-size:14px;padding:18px 30px;display:flex;justify-content:space-between}
.footer nav{display:flex;gap:20px}
.footer nav a{text-decoration:underline}
</style>
</head>
<body>
<div class="page">
  <header>
    <div class="abs brand"><div class="brand-dot"></div><div class="brand-name">Kessler-Volkshochschule<span>Kreis Aurental</span></div></div>
    <div class="abs search">Suche
      <svg width="28" height="28" viewBox="0 0 28 28" fill="none" stroke="#0b3272" stroke-width="2"><circle cx="16" cy="11" r="8"/><line x1="10" y1="17" x2="3" y2="25"/></svg>
    </div>
    <nav class="abs meta-nav"><span>Öffnungszeiten</span><span>Kontakt</span><span>Impressum</span></nav>
    <nav class="abs main-nav"><span>Startseite</span><span>Kursprogramm</span><span>Förderungen</span><span>Service</span><span>Unterrichtsstätten</span></nav>
  </header>

  <section>
    <div class="abs photo-left" role="img" aria-label="Foto: lächelndes Paar in Businesskleidung"></div>
    <div class="abs photo-center" role="img" aria-label="Foto: junge Teilnehmerin im Kursraum"></div>
    <div class="abs tile portal">
      <h2>Teilnehmer-<br>Portal</h2>
      <div class="field">Teilnehmer Nr.</div>
      <div class="field">Passwort</div>
      <div class="portal-links"><a>Teilnehmer Nummer vergessen?</a><a>Passwort vergessen?</a><a>Erstregistrierung</a></div>
      <span class="btn">Login</span>
    </div>
    <div class="abs tile akademie notch">
      <h2>Akademietage</h2>
      <p>Einladung zu den<br>8. Akademietagen in<br>Lindenau-Hofstetten</p>
      <span class="btn">Mehr erfahren</span>
    </div>
    <div class="abs brochure" role="img" aria-label="Titelblatt des Programmhefts mit bunter Schrift"></div>
    <div class="abs tile program notch">
      <h2>Programmheft</h2>
      <p>Hier können Sie das aktuelle<br>Programmheft als PDF<br>downloaden</p>
      <span class="btn">Jetzt downloaden</span>
    </div>
  </section>

  <section>
    <div class="abs courses-head">Kurse nach Fachbereichen</div>
    <div class="abs courses">
      <div class="arrow-btn" style="left:22px">‹</div>
      <div class="arrow-btn" style="right:22px">›</div>
      <div class="course" style="left:70px"><div class="circle" role="img" aria-label="Symbol Fachbereich Beruf" style="background:var(--beruf)"></div>Beruf</div>
      <div class="course" style="left:248px"><div class="circle" role="img" aria-label="Symbol Fachbereich Sprachen" style="background:var(--sprachen)"></div>Sprachen</div>
      <div class="course" style="left:426px"><div class="circle" role="img" aria-label="Symbol Fachbereich Gesundheit" style="background:var(--gesundheit)"></div>Gesundheit</div>
      <div class="course" style="left:604px"><div class="circle" role="img" aria-label="Symbol Fachbereich Kultur" style="background:var(--kultur)"></div>Kultur</div>
      <div class="course" style="left:782px"><div class="circle" role="img" aria-label="Symbol Fachbereich Gesellschaft" style="background:var(--gesellschaft)"></div>Gesellschaft</div>
      <div class="course" style="left:960px"><div class="circle" role="img" aria-label="Symbol Fachbereich Grundbildung" style="background:var(--grundbildung)"></div>Grundbildung</div>
    </div>
  </section>

  <section>
    <div class="abs tile news-head">
      <h2>Aktuelle News<br>der VHS</h2>
      <span class="btn">Alle News anzeigen</span>
    </div>
    <div class="abs news-list">
      <div class="news-item"><h3>Medien/Film</h3><p>Wir drehen einen Knettrickfilm<br>für Kinder ab 8 Jahren<br>Erlbach am Auen</p><a>Mehr erfahren</a></div>
      <div class="news-item"><h3>Fremde Länder</h3><p>Kilimandscharo<br>Grünwiesen</p><a>Mehr erfahren</a></div>
      <div class="news-item"><h3>Kunstgeschichte</h3><p>Emil Varden - Maler des<br>modernen Lebens<br>Lindenau-Hofstetten</p><a>Mehr erfahren</a></div>
    </div>
    <div class="abs tile jobs">
      <h2>Stellenbörse</h2>
      <p>Entdecken Sie unser<br>attracktives Jobangebot</p>
      <span class="btn">Jobs finden</span>
    </div>
    <div class="abs date"><span class="day">30</span><span class="month">Oktober</span></div>
    <div class="abs calendar">
      <h4>Oktober 2014</h4>
      <div class="cal-nav"><span></span><span></span></div>
      <div class="days">
        <span></span><span></span><span>01</span><span>02</span><span>03</span><span>04</span><span>05</span>
        <span>06</span><span>07</span><span>08</span><span>09</span><span>10</span><span>11</span><span>12</span>
        <span>13</span><span>14</span><span>15</span><span>16</span><span>17</span><span>18</span><span>19</span>
        <span>20</span><span>21</span><span>22</span><span>23</span><span>24</span><span>25</span><span>26</span>
        <span>27</span><span>28</span><span>29</span><span class="today">30</span><span>31</span>
      </div>
    </div>
    <div class="abs photo-dance" role="img" aria-label="Foto: tanzendes Paar in festlicher Kleidung"><span class="btn">Mehr erfahren</span></div>
    <div class="abs tile top">
      <h2>TOP-<br>Veranstaltug<br>des Monats</h2>
      <p>Tänze für festliche Anlässe<br>Standard- und Lateintänze<br>für Paare ohne Vorkenntnisse</p>
    </div>
  </section>

  <footer class="abs footer">
    <span>Copyright © 2014 Kessler Volkshochschule</span>
    <nav><a>Kontakt</a><a>Partner</a><a>AGB</a><a>Impressum</a><a>Widerruf</a></nav>
  </footer>
</div>
</body>
</html>
```